Escape Room Brochure, Trifold. Bold Black, yellow red. Doors Keys

We need a brochure to introduce our escape room and our services.
Attached are some of our designs as well as some examples of brochures we like.
We are THE VAULTS of KMD, however, we are aiming at Can you outwit the vaults of KMD.
We are one of three escape rooms in a college town. We believe our rooms are more creative and original. Only family friendly. Brochure to be distributed to explain what an escape room is and promote our new fundraising program.

Font styles to use
Other font styles liked:
• impact

Colors
fbee3e
ec1f27
000000
dbdbdb

Requirements
Must have
• description of our rooms. services we offer. Fundraising and group teambuilding. Most information can be found at thevaultsofkmd.example
• what is an escape room.
Nice to have
• Photoshop
Should not have
• padlock or maze

```html
<!DOCTYPE html>
<html lang="en">
<head>
<meta charset="utf-8">
<title>THE VAULTS of KMD – Trifold Brochure</title>
<link rel="stylesheet" href="https://fonts.googleapis.com/css2?family=Anton&family=Questrial&display=swap">
<style>
  :root {
    --yellow: #fbee3e;
    --red: #ec1f27;
    --black: #000000;
    --ink: #1c1c1c;
    --panel-dark: #2a2a2a;
    --grey: #dbdbdb;
    --paper: #ffffff;
    --text: #3a3a3a;
  }
  * { box-sizing: border-box; margin: 0; padding: 0; }
  html, body { width: 1200px; height: 800px; overflow: hidden; }
  body {
    background: var(--grey);
    font-family: "Questrial", "Century Gothic", sans-serif;
    display: flex;
    align-items: center;
    justify-content: center;
  }
  .brochure {
    width: 1140px;
    height: 740px;
    display: grid;
    grid-template-columns: repeat(3, 1fr);
    box-shadow: 0 10px 30px rgba(0,0,0,.25);
  }
  .panel { position: relative; height: 740px; overflow: hidden; }
  .panel--light { background: var(--paper); color: var(--text); display: flex; flex-direction: column; }
  .panel--dark { background: var(--panel-dark); color: #fff; }

  .heading, .label, .cta, .fundraising {
    font-family: "Anton", "Impact", sans-serif;
    font-weight: 400;
    text-transform: uppercase;
    letter-spacing: .5px;
  }
  .heading-band {
    background: var(--ink);
    padding: 22px 24px 18px;
    border-bottom: 4px solid var(--red);
  }
  .heading-band .heading { color: var(--yellow); font-size: 28px; line-height: 1; }

  .label {
    display: inline-block;
    align-self: flex-start;
    background: var(--yellow);
    color: var(--black);
    font-size: 20px;
    padding: 5px 14px 3px;
    line-height: 1.1;
  }
  .copy {
    font-size: 12px;
    line-height: 1.45;
    padding: 0 24px;
  }
  .copy p + p { margin-top: 9px; }
  .copy strong { color: var(--red); font-weight: 400; }

  /* left panel */
  .intro { padding-top: 14px; }
  .theme-block { margin-top: 16px; display: flex; flex-direction: column; }
  .theme-block .label { margin: 0 0 8px 24px; }
  .collage {
    flex: 1;
    min-height: 120px;
    margin-top: 12px;
    background: linear-gradient(120deg, #7b4bb8 0%, #e23a2f 30%, #f4c21c 55%, #3a7be0 80%, #1f9e55 100%);
  }
  .contact-line {
    flex: 0 0 48px;
    display: flex; align-items: center; justify-content: center; gap: 10px;
    font-size: 20px; color: var(--ink);
  }

  /* middle panel */
  .services-title { text-align: center; padding-top: 42px; font-size: 28px; color: #fff; }
  .service-map {
    position: absolute;
    left: 0; right: 0; top: 110px;
    height: 400px;
  }
  .service-map__backdrop {
    position: absolute;
    left: 20px; right: 20px; top: 70px; bottom: 70px;
    background: radial-gradient(circle at 60% 50%, #6a6a6a 0%, #3b3b3b 55%, #2a2a2a 100%);
  }
  .service-map svg { position: absolute; inset: 0; }
  .service-map .node-label {
    font-family: "Anton", "Impact", sans-serif;
    fill: var(--yellow);
    font-size: 13px;
  }
  .service-map .brand-name {
    font-family: "Anton", "Impact", sans-serif;
    fill: var(--yellow);
    font-size: 13px;
  }
  .cta {
    position: absolute;
    left: 0; right: 0; bottom: 96px;
    text-align: center;
    color: var(--yellow);
    font-size: 54px;
    line-height: 1;
  }
  .fundraising {
    position: absolute;
    left: 0; right: 0; bottom: 56px;
    text-align: center;
    color: var(--red);
    font-size: 16px;
  }

  /* right panel */
  .room { flex: 1; display: flex; flex-direction: column; padding-top: 24px; }
  .room .label { margin: 0 0 8px 24px; }
  .room-photo { flex: 1; min-height: 110px; margin-top: 12px; }
  .room-photo--virus { background: linear-gradient(135deg, #dfe6ee 0%, #8fa3bd 45%, #4f6787 100%); }
  .room-photo--basement { background: linear-gradient(160deg, #8a8173 0%, #5c5548 45%, #3a342c 100%); }
  .web-line {
    flex: 0 0 48px;
    display: flex; align-items: center; justify-content: center; gap: 10px;
    font-family: "Anton", "Impact", sans-serif;
    font-size: 18px; color: var(--ink);
  }
</style>
</head>
<body>
<main class="brochure">

  <section class="panel panel--light panel--intro">
    <header class="heading-band"><h1 class="heading">What is escape room?</h1></header>
    <div class="copy intro">
      <p>Our 'Escape the 90's' escape game is fun for all ages. Families and groups of 90's kids have been enjoying this room since March 2016. The Deadly Virus' escape room has been open since July 2016, and groups have been enjoying the extra challenge and complex medical/science themed clues.</p>
      <p>We are also proud to announce that The Basement of Horror is NOW OPEN. Customers have been enjoying the scary, horror-movie style atmosphere! THE VAULTS of KMD is a family business. We are proud to offer something for everyone, from <strong>group team building</strong> to our new <strong>fundraising program</strong>.</p>
    </div>
    <div class="theme-block">
      <h2 class="label">Escape the 90's</h2>
      <p class="copy">Jessica loves the 90's. You could say she's stuck there, and she wants your company. Locked in her apartment, you will have only 1 hour to find clues and solve puzzles to unlock the door, otherwise, the time machine she has been working on for all these years will be activated and you will be sent back for eternity to the 90s, the age of hedgehogs, beepers, singing purple dinosaurs, cassette tapes, and inflatable furniture.</p>
    </div>
    <div class="collage" role="img" aria-label="Colourful collage of 1990s toys, games and cartoon characters"></div>
    <div class="contact-line">
      <svg width="18" height="18" viewBox="0 0 24 24" aria-hidden="true"><path fill="#ec1f27" d="M6.6 10.8a15 15 0 0 0 6.6 6.6l2.2-2.2c.3-.3.7-.4 1-.2 1.1.4 2.3.6 3.6.6.6 0 1 .4 1 1V20c0 .6-.4 1-1 1A17 17 0 0 1 3 4c0-.6.4-1 1-1h3.5c.6 0 1 .4 1 1 0 1.3.2 2.5.6 3.6.1.3 0 .7-.2 1z"/></svg>
      <span>(555) 014-7210</span>
    </div>
  </section>

  <section class="panel panel--dark panel--services">
    <h2 class="heading services-title">What you get?</h2>
    <div class="service-map">
      <div class="service-map__backdrop" role="img" aria-label="Dim photo of a figure standing behind iron gates"></div>
      <svg viewBox="0 0 380 400" width="380" height="400">
        <g stroke="#ffffff" stroke-width="2">
          <line x1="190" y1="200" x2="190" y2="70"/>
          <line x1="190" y1="200" x2="305" y2="120"/>
          <line x1="190" y1="200" x2="315" y2="250"/>
          <line x1="190" y1="200" x2="235" y2="330"/>
          <line x1="190" y1="200" x2="95" y2="320"/>
          <line x1="190" y1="200" x2="70" y2="160"/>
        </g>
        <circle cx="190" cy="200" r="52" fill="#000" stroke="#fff" stroke-width="4"/>
        <text class="brand-name" x="190" y="196" text-anchor="middle">THE VAULTS</text>
        <text class="brand-name" x="190" y="214" text-anchor="middle">of KMD</text>

        <g fill="#fff" stroke="#000" stroke-width="1">
          <circle cx="190" cy="70" r="19"/>
          <circle cx="305" cy="120" r="19"/>
          <circle cx="315" cy="250" r="19"/>
          <circle cx="235" cy="330" r="19"/>
          <circle cx="95" cy="320" r="19"/>
          <circle cx="70" cy="160" r="19"/>
        </g>
        <g fill="#000">
          <circle cx="184" cy="66" r="3.5"/><circle cx="196" cy="66" r="3.5"/>
          <rect x="178" y="71" width="12" height="6" rx="3"/><rect x="190" y="71" width="12" height="6" rx="3"/>
          <circle cx="300" cy="114" r="3"/><circle cx="310" cy="114" r="3"/>
          <rect x="296" y="119" width="8" height="10" rx="2"/><rect x="306" y="119" width="8" height="10" rx="2"/>
          <rect x="306" y="248" width="18" height="9"/><rect x="309" y="244" width="2" height="5"/><rect x="314" y="244" width="2" height="5"/><rect x="319" y="244" width="2" height="5"/>
          <rect x="86" y="311" width="18" height="18" rx="2"/>
          <rect x="62" y="153" width="15" height="14" rx="2"/><circle cx="79" cy="160" r="3"/>
        </g>
        <text x="95" y="325" text-anchor="middle" fill="#fff" font-family="Anton, sans-serif" font-size="14">?</text>
        <g fill="none" stroke="#000" stroke-width="2.5">
          <circle cx="232" cy="327" r="6"/><line x1="237" y1="332" x2="242" y2="338"/>
        </g>

        <text class="node-label" x="190" y="38" text-anchor="middle">Team Building</text>
        <text class="node-label" x="305" y="90" text-anchor="middle">Date Night</text>
        <text class="node-label" x="315" y="290" text-anchor="middle">Parties</text>
        <text class="node-label" x="235" y="370" text-anchor="middle">Mysteries</text>
        <text class="node-label" x="95" y="362" text-anchor="middle">Riddles</text>
        <text class="node-label" x="70" y="128" text-anchor="middle">Puzzles</text>
      </svg>
    </div>
    <p class="cta">Book now</p>
    <p class="fundraising">Ask about our fundraising program</p>
  </section>

  <section class="panel panel--light panel--rooms">
    <article class="room">
      <h2 class="label">The deadly virus</h2>
      <p class="copy">Millions of people across the world have been infected with a life-threatening virus. Dr. Martin Hale from Vela Pharmaceuticals was working on a cure that could save lives across the globe, but has just recently died, presumably from the very disease he was trying to cure. You and your team have been tasked with looking into the death of Dr. Hale. What you learn will put you and your friends at risk, as you shed light on a larger conspiracy.</p>
      <div class="room-photo room-photo--virus" role="img" aria-label="Photo of a gloved hand pressed against glass in a hazmat lab"></div>
    </article>
    <article class="room">
      <h2 class="label">The basement of horror</h2>
      <p class="copy">On a quest to save your friend, you find yourself trapped in the lair of a murderous psychopath. As you search for a way to escape, you must find out where your friend is and how to save them. Will you be able to stop this maniac, or will you soon need a friend to save you?</p>
      <div class="room-photo room-photo--basement" role="img" aria-label="Photo of a grimy, bloodstained basement corridor"></div>
    </article>
    <div class="web-line">
      <svg width="16" height="16" viewBox="0 0 24 24" aria-hidden="true"><g fill="none" stroke="#ec1f27" stroke-width="2"><circle cx="12" cy="12" r="10"/><ellipse cx="12" cy="12" rx="4" ry="10"/><line x1="2" y1="12" x2="22" y2="12"/></g></svg>
      <span>www.thevaultsofkmd.example</span>
    </div>
  </section>

</main>
</body>
</html>
```